Linked In Profile Banner Needed

I am in need of a Linked In Banner photo for my profile. The dimensions are 1584 x 396 pixels and the bottom left is where Linked In places my photo over so be aware of that. I attached an example for your reference.

I have also attached my logo and business card so you can keep the same color & style conistant.

Also add the following text:

"Preserve capital with a tax advantaged lease for equipment, vehicles, software and more! $5,000 - $50m"

You can also look at our website here:
www.HarlowfieldFundingCo.com

```html
<!DOCTYPE html>
<html lang="en">
<head>
<meta charset="utf-8">
<title>Harlowfield Funding Co. — Profile Banner</title>
<link href="https://fonts.googleapis.com/css2?family=Montserrat:ital,wght@0,400;0,500;0,700;1,400&display=swap" rel="stylesheet">
<style>
  :root {
    --backdrop: #b8ecfa;
    --navy-light: #262a4a;
    --navy-mid: #1f1d38;
    --navy-dark: #16132e;
    --accent: #4ab8df;
    --divider: #3a8fb8;
    --white: #ffffff;
    --mark: #3a8fd6;
  }
  * { margin: 0; padding: 0; box-sizing: border-box; }
  html, body {
    width: 1200px;
    height: 1200px;
    overflow: hidden;
    background: var(--backdrop);
    font-family: "Montserrat", Arial, sans-serif;
  }
  .banner {
    position: absolute;
    left: 60px;
    top: 465px;
    width: 1080px;
    height: 270px;
    background: linear-gradient(90deg, var(--navy-light) 0%, var(--navy-mid) 45%, var(--navy-dark) 100%);
    overflow: hidden;
  }
  .banner__message {
    position: absolute;
    right: 323px;
    top: 70px;
    text-align: right;
  }
  .banner__tagline {
    color: var(--accent);
    font-style: italic;
    font-weight: 400;
    font-size: 19px;
    line-height: 25px;
    letter-spacing: 0.1px;
  }
  .banner__range {
    margin-top: 10px;
    color: var(--white);
    font-weight: 700;
    font-size: 35px;
    line-height: 40px;
  }
  .banner__divider {
    position: absolute;
    left: 787px;
    top: 68px;
    width: 1px;
    height: 137px;
    background: var(--divider);
  }
  .brand {
    position: absolute;
    left: 817px;
    top: 113px;
    display: flex;
    align-items: center;
    gap: 10px;
  }
  .brand__square {
    width: 30px;
    height: 30px;
    background: var(--mark);
  }
  .brand__name {
    color: var(--white);
    font-weight: 500;
    font-size: 19px;
    line-height: 22px;
    letter-spacing: 0.3px;
  }
  .brand__name span {
    display: block;
    font-size: 10px;
    line-height: 14px;
    letter-spacing: 4px;
    text-align: center;
  }
</style>
</head>
<body>
  <section class="banner" aria-label="Profile banner">
    <div class="banner__message">
      <p class="banner__tagline">Preserve capital with a tax advantaged lease for<br>equipment, vehicles, software<br>and more!</p>
      <p class="banner__range">$5,000 - $50m</p>
    </div>
    <div class="banner__divider"></div>
    <div class="brand">
      <div class="brand__square"></div>
      <p class="brand__name">HARLOWFIELD FUNDING<span>COMPANY</span></p>
    </div>
  </section>
</body>
</html>
```